Music Festival Business Cards

The Lanternmoor Festival
Produced by Bramblewick Sound Group LLC
New music festival in Arkansas.

Target Market(s)

18-35 year olds

Industry/Entity Type

Festival

Contact Information for Business Card

We are a 5-partner team producing a music festival in Arkansas. We need slick business cards, and I want them to be square.

Requirements
Must have
• I NEED THESE TO BE IN SQUARE SIZE - 2x2 or 2.5x2.5... please not regular size.
• I need www.thelanternmoor.live as the link to website.

```html
<!DOCTYPE html>
<html lang="en">
<head>
<meta charset="utf-8">
<title>The Lanternmoor Festival – Business Cards</title>
<link rel="stylesheet" href="https://fonts.googleapis.com/css2?family=Roboto:wght@400;500;700&display=swap">
<style>
  :root {
    --backdrop: #e7e2da;
    --card-dark: #1d1f20;
    --card-dark-edge: #2c2f31;
    --teal: #36cfd6;
    --white: #ffffff;
    --shadow: rgba(0,0,0,0.28);
  }
  * { box-sizing: border-box; margin: 0; padding: 0; }
  html, body {
    width: 1200px; height: 911px; overflow: hidden;
    background: var(--backdrop);
    font-family: "Roboto", Arial, sans-serif;
  }
  .canvas { position: relative; width: 1200px; height: 911px; }

  .card {
    position: absolute;
    width: 440px; height: 440px;
    border-radius: 6px;
    overflow: hidden;
    box-shadow: 0 14px 30px var(--shadow);
  }
  .card--front { left: 120px; top: 235px; background: var(--teal); }
  .card--back  { left: 640px; top: 235px; background: linear-gradient(160deg, var(--card-dark-edge), var(--card-dark) 55%); }

  .wordmark {
    color: var(--teal);
    font-weight: 500;
    text-transform: uppercase;
    white-space: nowrap;
  }

  /* front */
  .front__head {
    height: 190px;
    background: linear-gradient(160deg, var(--card-dark-edge), var(--card-dark) 60%);
    display: flex; align-items: center; justify-content: center; gap: 12px;
  }
  .front__head .wordmark { font-size: 26px; letter-spacing: 4px; }
  .wordmark__dot {
    width: 14px; height: 14px; border-radius: 50%;
    background: var(--teal);
  }
  .front__info {
    position: absolute; left: 30px; top: 418px;
    transform-origin: top left;
    transform: rotate(-90deg);
    color: var(--white);
    white-space: nowrap;
  }
  .person { margin-bottom: 14px; }
  .person__name { font-size: 19px; font-weight: 700; text-transform: uppercase; line-height: 1.2; }
  .person__role { font-size: 13px; font-weight: 500; text-transform: uppercase; }
  .address { font-size: 13px; line-height: 1.45; font-weight: 500; margin-bottom: 14px; }
  .contact-list { list-style: none; font-size: 12.5px; line-height: 1.55; font-weight: 500; }
  .contact-list li { display: flex; align-items: center; gap: 7px; }
  .contact-list svg { width: 11px; height: 11px; fill: var(--white); flex: none; }

  /* back */
  .back__title {
    position: absolute; left: 104px; top: 40px;
    transform-origin: top left;
    transform: rotate(90deg);
    white-space: nowrap;
  }
  .back__title .wordmark { display: block; font-size: 28px; letter-spacing: 5px; line-height: 1.2; }
  .back__url {
    display: block;
    color: var(--white);
    font-size: 12px; letter-spacing: 4px;
    margin-top: 4px;
  }
</style>
</head>
<body>
<main class="canvas">

  <section class="card card--front" aria-label="Business card front">
    <header class="front__head">
      <span class="wordmark__dot"></span>
      <span class="wordmark">The Lanternmoor</span>
    </header>
    <div class="front__info">
      <div class="person">
        <p class="person__name">Elias Marrow</p>
        <p class="person__role">CEO/Founder</p>
      </div>
      <p class="address">412 Cedar Hollow Road<br>Fayetteville, Arkansas 72701</p>
      <ul class="contact-list">
        <li><svg viewBox="0 0 24 24"><path d="M6.6 10.8a15 15 0 0 0 6.6 6.6l2.2-2.2c.3-.3.7-.4 1-.2 1.1.4 2.3.6 3.6.6.6 0 1 .4 1 1V20c0 .6-.4 1-1 1A17 17 0 0 1 3 4c0-.6.4-1 1-1h3.5c.6 0 1 .4 1 1 0 1.3.2 2.5.6 3.6.1.3 0 .7-.2 1z"/></svg>555 214 7730</li>
        <li><svg viewBox="0 0 24 24"><rect x="6" y="2" width="12" height="20" rx="2"/></svg>555 309 4418</li>
        <li><svg viewBox="0 0 24 24"><rect x="3" y="6" width="18" height="14" rx="1"/></svg>555 862 1057</li>
        <li><svg viewBox="0 0 24 24"><path d="M2 5h20v14H2z"/></svg>elias@thelanternmoor.live</li>
        <li><svg viewBox="0 0 24 24"><circle cx="12" cy="12" r="10"/></svg>www.thelanternmoor.live</li>
      </ul>
    </div>
  </section>

  <section class="card card--back" aria-label="Business card back">
    <div class="back__title">
      <span class="wordmark">The Lanternmoor</span>
      <span class="back__url">www.thelanternmoor.live</span>
    </div>
  </section>

</main>
</body>
</html>
```